Legislative compliance to home owners, landlords and agents

Logo, business card and stationaly header for a sole trader offering sevices in the UK to home owners, landlords and Letting agents to meet legislation requirement relating to sale and leasing of rental domestic homes. Services offered include Legionella Risk Assessment, Portable Appliance Testing and Energy Performance Certificates. Logo to include depiction of a house and compliance tick list images. Have an existing card with water splash image to reflect water testing, so considering picking up same wave blue. Company name Kestov Property Services. Web www.kestovps-example.com. email: info@kestovps-example.com. Address: Brackenlea, Aberdeen. All three services to be listed. Name as existing card.,

Target Market(s)

UK home owners, landlords, lettings and estate agents

Industry/Entity Type

Property Management

Contact Information for Business Card

Derek Moffatt CEng, MSFabTec
Address: Brackenlea, Aberdeen
Web: www.kestovps-example.com
e-mail info@kestovps-example.com
Phone: 07700 918 302
Services: Legionella Risk Assessment, Portable Appliance Testing, Energy Performance Certificate

Logo Text

Kestov Property Services

Font styles to use
Sans Serif

Colors

Designer to choose colors to be used in the design.

Requirements
Must have
• Suitable for standard UK business card size 85 mm x 55 mm, with allowance for safety border/ bleed such that colours extend to outside border of card once printed
Nice to have
• Clear font style and layout
• Happy to see images depicting phone, address etc

```html
<!DOCTYPE html>
<html lang="en">
<head>
<meta charset="utf-8">
<title>Kestov Property Services – Business Card</title>
<link href="https://fonts.googleapis.com/css2?family=Open+Sans:wght@400;600;700&display=swap" rel="stylesheet">
<style>
  :root {
    --navy: #26236f;
    --ink: #4a4a4a;
    --muted: #7a7a7a;
    --rule: #9c9ab8;
    --card: #ffffff;
    --backdrop: #e6e6e6;
  }
  html, body {
    margin: 0;
    width: 1200px;
    height: 1200px;
    overflow: hidden;
    background: var(--backdrop);
    font-family: "Open Sans", Arial, sans-serif;
  }
  .card {
    position: absolute;
    left: 100px;
    top: 277px;
    width: 1000px;
    height: 647px;
    background: var(--card);
    box-shadow: 0 8px 30px rgba(0,0,0,0.15);
    overflow: hidden;
  }
  .brand {
    position: absolute;
    left: 90px;
    top: 178px;
    display: flex;
    align-items: center;
    gap: 14px;
  }
  .brand-mark {
    width: 28px;
    height: 28px;
    background: var(--navy);
    flex: none;
  }
  .brand-name {
    font-weight: 700;
    font-size: 26px;
    color: var(--navy);
    white-space: nowrap;
  }
  .divider {
    position: absolute;
    width: 1.5px;
    background: var(--rule);
  }
  .divider.top { left: 540px; top: 140px; height: 95px; }
  .divider.bottom { left: 600px; top: 268px; height: 170px; }
  .person {
    position: absolute;
    left: 565px;
    top: 140px;
  }
  .person-name {
    margin: 0;
    font-size: 38px;
    font-weight: 700;
    color: var(--navy);
    letter-spacing: 0.5px;
    line-height: 1.1;
    white-space: nowrap;
  }
  .person-title {
    margin: 14px 0 0 22px;
    font-size: 21px;
    color: var(--muted);
  }
  .contacts {
    position: absolute;
    left: 620px;
    top: 272px;
    margin: 0;
    padding: 0;
    list-style: none;
    font-size: 22px;
    color: var(--ink);
  }
  .contacts li {
    display: flex;
    align-items: center;
    gap: 12px;
    height: 36px;
    white-space: nowrap;
  }
  .contacts li.gap { margin-top: 16px; }
  .contacts svg { width: 20px; height: 20px; fill: var(--navy); flex: none; }
  .services {
    position: absolute;
    left: 170px;
    top: 395px;
  }
  .services h2 {
    margin: 0 0 4px;
    font-size: 23px;
    font-weight: 700;
    color: var(--navy);
  }
  .services ul {
    margin: 0;
    padding: 0 0 0 26px;
    list-style: none;
    font-size: 23px;
    color: var(--ink);
    line-height: 1.35;
    white-space: nowrap;
  }
  .rule-line {
    position: absolute;
    left: 0; right: 0;
    top: 560px;
    height: 3px;
    background: var(--navy);
  }
  .band {
    position: absolute;
    left: 0; right: 0;
    top: 575px;
    bottom: 0;
    background: var(--navy);
  }
</style>
</head>
<body>
  <main class="card">
    <div class="brand">
      <span class="brand-mark"></span>
      <span class="brand-name">Kestov Property Services</span>
    </div>

    <span class="divider top"></span>
    <div class="person">
      <h1 class="person-name">DEREK MOFFATT</h1>
      <p class="person-title">CEng, MSFabTec</p>
    </div>

    <span class="divider bottom"></span>
    <ul class="contacts">
      <li>
        <svg viewBox="0 0 24 24" aria-hidden="true"><path d="M6.6 10.8a15.1 15.1 0 0 0 6.6 6.6l2.2-2.2a1 1 0 0 1 1-.25 11.4 11.4 0 0 0 3.6.57 1 1 0 0 1 1 1V20a1 1 0 0 1-1 1A17 17 0 0 1 3 4a1 1 0 0 1 1-1h3.5a1 1 0 0 1 1 1c0 1.25.2 2.45.57 3.57a1 1 0 0 1-.25 1z"/></svg>
        07700 918 302
      </li>
      <li>
        <svg viewBox="0 0 24 24" aria-hidden="true"><path d="M2 5h20v14H2V5zm2 2v.4l8 6 8-6V7l-8 6-8-6z"/></svg>
        info@kestovps-example.com
      </li>
      <li class="gap">
        <svg viewBox="0 0 24 24" aria-hidden="true"><circle cx="12" cy="12" r="9" fill="none" stroke="#26236f" stroke-width="2"/><path d="M3 12h18M12 3c3 3 3 15 0 18M12 3c-3 3-3 15 0 18" fill="none" stroke="#26236f" stroke-width="1.6"/></svg>
        www.kestovps-example.com
      </li>
      <li>
        <svg viewBox="0 0 24 24" aria-hidden="true"><path d="M12 3 2 12h3v9h5v-6h4v6h5v-9h3z"/></svg>
        Brackenlea, Aberdeen
      </li>
    </ul>

    <section class="services">
      <h2>SERVICE</h2>
      <ul>
        <li>Legionella Risk Assessment</li>
        <li>Portable Appliance Testing</li>
        <li>Energy Performance Certificate</li>
      </ul>
    </section>

    <span class="rule-line"></span>
    <span class="band"></span>
  </main>
</body>
</html>
```